A5, portrait
Theme is science
audience is VIPS, politicians, executives
this is a really important event, we want a very classy invitation
include logo for bloom and grow and lumen but lumen one bigger
images attached
Have attached some styles we like but doesn't need to be these colours. If we can incorporate some colours from our logo would be good but don't make too colourful and childish

You’re invited to the official opening and launch of Lumen, Centre of Discovery. an industry first, pioneering, STEM hub.

Saturday 30th April, 2022

10:00 am – 12:00 pm

42 Calder Lane, Wrenfield

Light canapes provided. Dress code is smart/casual

All guests will be given a guided walk through of Australia’s first dedicated STEM education hub for children aged 3-6.

Invitation only

RSVP: 18 April to marketing@bloomandgrow.edu.au

```html
<!DOCTYPE html>
<html lang="en">
<head>
<meta charset="utf-8">
<title>Lumen, Centre of Discovery – Official Opening Invitation</title>
<link rel="stylesheet" href="https://fonts.googleapis.com/css2?family=Catamaran:wght@400;700;900&family=Caveat+Brush&display=swap">
<style>
  :root {
    --space-deep: #1b1a55;
    --space-mid: #2a3596;
    --space-glow: #2f4db0;
    --text-light: #ffffff;
    --accent-yellow: #ffe500;
    --accent-cyan: #29b6e8;
    --cloud: #ffffff;
    --ink-navy: #1d1f4f;
    --planet-light: #f4f9ff;
    --planet-edge: #cfe6f8;
  }
  * { margin: 0; padding: 0; box-sizing: border-box; }
  html, body { width: 914px; height: 1200px; overflow: hidden; }
  body { font-family: "Catamaran", sans-serif; background: var(--space-deep); }

  .invitation {
    position: relative;
    width: 914px;
    height: 1200px;
    overflow: hidden;
    background:
      radial-gradient(ellipse 70% 40% at 50% 48%, var(--space-glow) 0%, rgba(47,77,176,0) 70%),
      linear-gradient(180deg, var(--space-mid) 0%, #27308a 45%, var(--space-deep) 100%);
    color: var(--text-light);
  }

  .brand {
    position: absolute;
    top: 76px;
    right: 43px;
    display: flex;
    align-items: center;
    gap: 8px;
    font-weight: 700;
    font-size: 24px;
    line-height: 1;
    color: var(--accent-yellow);
  }
  .brand-dot {
    width: 18px; height: 18px;
    border-radius: 50%;
    background: var(--accent-yellow);
  }

  .centered { position: absolute; left: 0; right: 0; text-align: center; }

  .intro {
    top: 148px;
    font-size: 26px;
    line-height: 1.05;
  }

  .planet-art {
    position: absolute;
    left: 319px; top: 229px;
    width: 321px; height: 211px;
    border-radius: 50%;
    background: radial-gradient(ellipse at 50% 45%, var(--planet-light) 0%, var(--planet-light) 50%, var(--planet-edge) 100%);
  }

  .event-wordmark {
    top: 452px;
    font-weight: 900;
    font-size: 172px;
    line-height: 1;
    letter-spacing: 2px;
    color: var(--accent-yellow);
  }

  .event-name {
    top: 601px;
    font-family: "Caveat Brush", cursive;
    font-weight: 400;
    font-size: 74px;
    line-height: 1;
  }
  .tagline {
    top: 678px;
    font-weight: 700;
    font-size: 32px;
    line-height: 1;
    color: var(--accent-yellow);
  }

  .when {
    top: 746px;
    font-size: 36px;
    line-height: 1.1;
  }
  .where {
    top: 831px;
    font-size: 40px;
    line-height: 1;
  }
  .notes {
    top: 895px;
    font-size: 26px;
    line-height: 1;
    color: var(--accent-cyan);
  }
  .details {
    top: 934px;
    font-size: 26px;
    line-height: 1.33;
  }

  .cloud-bank { position: absolute; left: 0; bottom: 0; width: 914px; height: 180px; }

  .rsvp {
    top: 1066px;
    font-size: 22px;
    line-height: 1.2;
    color: var(--ink-navy);
  }
  .rsvp .invite-only { margin-bottom: 9px; }
</style>
</head>
<body>
  <main class="invitation">
    <div class="brand"><span class="brand-dot"></span>bloom and grow</div>

    <p class="centered intro">You’re invited to the<br>official opening and launch of</p>

    <div class="planet-art" role="img" aria-label="Illustration of a bright ringed planet with coloured stars and a small rocket"></div>

    <h1 class="centered event-wordmark">LUMEN</h1>
    <p class="centered event-name">Centre of Discovery</p>
    <p class="centered tagline">an industry first, pioneering, STEM hub</p>

    <p class="centered when">Saturday 30th April, 2022<br>10:00 a.m. – 12:00 p.m.</p>
    <p class="centered where">42 Calder Lane, Wrenfield</p>

    <p class="centered notes">Light canapes provided. Dress code is smart/casual</p>
    <p class="centered details">All guests will be given a guided walk through of Australia’s first<br>dedicated STEM education hub for children aged 3-6.</p>

    <svg class="cloud-bank" viewBox="0 1020 914 180" aria-hidden="true">
      <g fill="var(--cloud)">
        <ellipse cx="460" cy="1180" rx="200" ry="143"/>
        <ellipse cx="300" cy="1210" rx="115" ry="100"/>
        <ellipse cx="630" cy="1210" rx="115" ry="100"/>
        <ellipse cx="110" cy="1230" rx="150" ry="80"/>
        <ellipse cx="820" cy="1228" rx="140" ry="78"/>
      </g>
    </svg>

    <div class="centered rsvp">
      <p class="invite-only">Invitation only</p>
      <p>RSVP:<br>18 April to marketing@bloomandgrow.edu.au</p>
    </div>
  </main>
</body>
</html>
```